One of a kind, 100% Pure & Natural Skincare line needs stunning product label

We need product label design for new natural skincare company called Tobin & Lusa Skincare. We create luxurious, 100% pure & natural skincare that is free from ingredients that may be potentially irritating to the skin. No toxins, preservatives or additives. Our initial product is Meadowlight Face Balm, a nourishing face cream that suits discerning women with mature skin and those with dry/sensitive skin needing extra hydration. Also those that choose to minimize their exposure to environmental toxins. Our brand is simple yet elegant, supporting a holistic, authentic lifestyle and embracing natural skincare.

Target Market(s)

Discerning women with mature skin and those with dry/sensitive skin needing extra hydration. Also those that choose to minimize their exposure to environmental toxins.

Industry/Entity Type

Skin Care Product

Font styles to use
Sans Serif
Script

Colors
f9d9e8
fef1ee

Requirements
Must have
• The Logo.
MEADOWLIGHT FACE BALM
EMBRACING NATURAL SKINCARE
Labels must be feminine, simple/minimal yet stylish. Uncluttered yet elegant.
This is a very natural product with minimal ingredients.
Nice to have
• The logo can be incorporated in to the label, or It can be left separate as a sticker on top of the jar. The product is a firm balm consistency and is in frosted glass jars with matt silver lids.
Jar height is 45mm, width is 60mm.
Label height: 28mm and length 185mm
Should not have
• Natural or farmers market type theme. No Bold/loud lettering.

```html
<!DOCTYPE html>
<html lang="en">
<head>
<meta charset="utf-8">
<title>Meadowlight Face Balm – Label</title>
<link href="https://fonts.googleapis.com/css2?family=Montserrat:wght@400;600&display=swap" rel="stylesheet">
<style>
  :root {
    --page: #ffffff;
    --ink: #2b2b2b;
    --muted: #555555;
    --label-border: #8a8a8a;
    --bleed-line: #bcd6e6;
    --safe-line: #c9dcea;
    --blush-deep: #f3bccb;
    --blush-soft: #f9d9e8;
    --white: #ffffff;
    --brand-pink: #e7a9b9;
  }
  * { box-sizing: border-box; margin: 0; padding: 0; }
  html, body {
    width: 1200px; height: 1000px; overflow: hidden;
    background: var(--page);
    font-family: "Montserrat", Arial, sans-serif;
    color: var(--ink);
  }
  .canvas { position: relative; width: 1200px; height: 1000px; }

  .bleed-outline {
    position: absolute; left: 40px; top: 398px; width: 1132px; height: 204px;
    border: 1px dashed var(--bleed-line);
  }
  .label {
    position: absolute; left: 64px; top: 417px; width: 1096px; height: 166px;
    border: 1px solid var(--label-border);
    background: var(--white);
    overflow: hidden;
  }
  .front-panel {
    position: absolute; left: 343px; top: 0; width: 420px; height: 100%;
    background: linear-gradient(90deg, var(--blush-deep) 0%, var(--blush-soft) 45%, #fdf0f4 75%, var(--white) 100%);
  }
  .safe-zone {
    position: absolute; top: 18px; height: 129px;
    border: 1px dashed var(--safe-line);
  }
  .safe-zone.left { left: 14px; width: 320px; }
  .safe-zone.right { left: 744px; width: 325px; }

  .info-column {
    position: absolute; font-size: 10px; line-height: 13px; color: var(--ink);
  }
  .info-column strong { font-weight: 600; }
  .info-column p { margin-bottom: 10px; }
  .info-column.left { left: 19px; top: 24px; width: 300px; }
  .info-column.right { left: 747px; top: 22px; width: 320px; }
  .info-column.right p { margin-bottom: 9px; }
  .info-column.right p.tight { margin-bottom: 6px; }

  .brand-mark {
    position: absolute; left: 0; top: 30px; width: 100%;
    display: flex; justify-content: center; align-items: center; gap: 5px;
    font-size: 9px; color: var(--brand-pink); letter-spacing: 0.2px;
  }
  .brand-dot { width: 7px; height: 7px; border-radius: 50%; background: var(--brand-pink); }
  .product-name {
    position: absolute; left: 0; top: 71px; width: 100%; text-align: center;
    font-size: 21px; font-weight: 400; letter-spacing: 0.3px; color: var(--ink);
  }
  .name-rule {
    position: absolute; left: 84px; top: 96px; width: 232px; height: 1px; background: var(--ink);
  }
  .tagline {
    position: absolute; left: 0; top: 100px; width: 100%; text-align: center;
    font-size: 8px; letter-spacing: 0.3px; color: var(--muted);
  }
  .volume {
    position: absolute; left: 0; top: 130px; width: 100%; text-align: center;
    font-size: 6.5px; color: var(--ink);
  }
  .pao-icon { position: absolute; left: 1036px; top: 119px; }
</style>
</head>
<body>
<div class="canvas">
  <div class="bleed-outline"></div>
  <div class="label">
    <div class="front-panel">
      <div class="brand-mark"><span class="brand-dot"></span><span>Tobin &amp; Lusa Skincare</span></div>
      <h1 class="product-name">MEADOWLIGHT FACE BALM</h1>
      <div class="name-rule"></div>
      <p class="tagline">EMBRACING NATURAL SKINCARE</p>
      <p class="volume">50 ml</p>
    </div>
    <div class="safe-zone left"></div>
    <div class="safe-zone right"></div>

    <div class="info-column left">
      <p><strong>INGREDIENTS :</strong>&nbsp; Tallow from pasture raised goats, frankincense, sandalwood &amp; myrrh essential oils.</p>
      <p><strong>DIRECTIONS :</strong>&nbsp; Soften small amount in palm of<br>hand &amp; gently massage into skin as often as</p>
      <p style="margin-top:16px">Allergy patch test recommended. If irritation occurs, discon-<br>tinue use.</p>
    </div>

    <div class="info-column right">
      <p><strong>CAUTION:</strong>&nbsp; Keep out of reach of children. If pregnant or breastfeeding, consult your healthcare practitioner. Avoid contact with eyes &amp; sensitive areas.</p>
      <p>Store below 25°C</p>
      <p class="tight">MADE IN AUSTRALIA</p>
      <p class="tight">B#</p>
      <p>info@tobinandlusaskincare.com.au</p>
    </div>

    <svg class="pao-icon" width="24" height="22" viewBox="0 0 24 22" aria-label="Period after opening: 6 months">
      <path d="M3 9 L21 9 L20 20 L4 20 Z" fill="none" stroke="#2b2b2b" stroke-width="1.2"/>
      <path d="M4 7 L19 2" fill="none" stroke="#2b2b2b" stroke-width="1.4"/>
      <text x="12" y="17.5" text-anchor="middle" font-size="6" font-family="Montserrat, Arial, sans-serif" font-weight="600" fill="#2b2b2b">6M</text>
    </svg>
  </div>
</div>
</body>
</html>
```